Brochure Design Project for Home Watch company

We are a new start up company in fast growing home watch industry. We provide services in Hawaii so the design needs to be reflect that. Our web site can give you overview of what we do - www.palmcrestkeeper.com. We will service clients that own second homes in Hawaii. These properties are not necessarily income producing properties for our clients. I'm looking for 2 or 4 page brochure which will be used to market our services to potential new clients. It needs to be high quality, modern with slight Hawaiian feel (we are based on Oahu). I'm not looking for a trifold type of brochure.

We are open to various colors based on what the designer might suggest but as you can see on our home page - the main picture of the home on our site has lots of red and white which we like as well as the "head" or dot above the "i" in our logo is red. I was not able to upload the file of the main house (purchased on snapvaultpix) on here therefore I'll have to provide the original photo to the selected designer at the later time. For now I just uploaded the not purchased copy.

If you have other questions please do let me know. And lastly, I will be looking to create a business card and post card as well.

```html
<!DOCTYPE html>
<html lang="en">
<head>
<meta charset="utf-8">
<title>Palm Crest Keeper — Brochure</title>
<link href="https://fonts.googleapis.com/css2?family=Montserrat:wght@500;600;700&family=Didact+Gothic&display=swap" rel="stylesheet">
<style>
:root{
  --red:#e2474d;
  --wine:#7a1f2b;
  --blue:#1f5ea8;
  --ink:#3a3a3a;
  --paper:#ffffff;
  --sky:#3f7fc4;
  --pool:#2a6a8c;
}
*{box-sizing:border-box;margin:0;padding:0}
html,body{width:960px;height:1200px;overflow:hidden}
body{background:linear-gradient(180deg,#e6e6e6,#d2d2d2);font-family:"Didact Gothic",sans-serif;color:var(--ink);position:relative}
.spread{position:absolute;left:100px;width:760px;height:520px;display:flex;box-shadow:0 10px 28px rgba(0,0,0,.18)}
.spread--outer{top:50px}
.spread--inner{top:630px}
.page{position:relative;width:380px;height:520px;background:var(--paper);overflow:hidden}
.page + .page{border-left:1px solid #ececec}
.heading{font-family:"Montserrat",sans-serif;font-weight:500}
p{font-size:10px;line-height:1.45}

/* back cover */
.back__band{position:absolute;left:0;top:0;bottom:0;width:18px;background:var(--red)}
.back__body{position:absolute;left:46px;right:34px;top:110px}
.back__title{color:var(--red);font-size:17px;margin-bottom:12px}
.contact{margin-top:40px;list-style:none}
.contact li{display:flex;align-items:center;gap:10px;font-size:11px;margin-bottom:7px}
.contact svg{width:14px;height:14px;flex:none}
.contact .phone{color:var(--red);font-family:"Montserrat",sans-serif;font-weight:600}
.badge{margin-top:26px;width:130px;height:34px;background:#e9eef5;border-left:6px solid var(--blue)}
.back__note{margin-top:12px;font-size:8.5px;color:#666}

/* front cover */
.front__photo{position:absolute;inset:0;background:linear-gradient(180deg,var(--sky) 0%,#8fbde6 38%,#d9d6cf 55%,#5d8fa6 72%,var(--pool) 100%)}
.front__strip{position:absolute;left:0;top:0;bottom:0;width:62px;background:rgba(122,31,43,.82)}
.brand{position:absolute;left:96px;top:40px;display:flex;align-items:center;gap:10px;color:#fff}
.brand__mark{width:22px;height:22px;border:2px solid #fff}
.brand__name{font-family:"Montserrat",sans-serif;font-weight:600;font-size:13px}
.brand__tag{position:absolute;left:96px;top:70px;color:#fff;font-size:9px}
.front__title{position:absolute;left:80px;right:20px;bottom:44px;color:#fff;font-family:"Montserrat",sans-serif;font-weight:700;font-size:17px;line-height:1.25}

/* inner spread */
.band{position:absolute;left:0;right:0;top:0;background:var(--red);color:#fff}
.band--left{height:114px;padding:22px 30px 0}
.band--left p{width:196px;font-size:9px;line-height:1.4}
.band--right{height:86px;padding:26px 24px 0}
.band__title{font-size:18px;margin-bottom:6px}
.band p{font-size:9.5px}
.devices{position:absolute;left:238px;top:44px;width:126px;height:98px;border-radius:6px;background:linear-gradient(160deg,#2b2b2b,#6e7780 60%,#d9dde2)}
.services{position:absolute;left:30px;top:130px;width:200px}
.service{margin-bottom:12px}
.service__title{color:var(--blue);font-family:"Montserrat",sans-serif;font-weight:700;font-size:10.5px;line-height:1.25;margin-bottom:4px}
.services .service p{font-size:8.5px;line-height:1.35}
.tab{position:absolute;left:24px;top:76px;background:var(--paper);padding:5px 12px;color:var(--red);font-family:"Montserrat",sans-serif;font-weight:700;font-size:11px}
.concierge{position:absolute;left:24px;right:24px;top:112px}
.concierge .service p{font-size:8.8px}
.concierge .service--wide{margin-left:110px}
.house{position:absolute;background:linear-gradient(180deg,#d8dadd,#bfc3c8);border-top:6px solid var(--red)}
.house--left{left:240px;right:0;top:200px;height:290px}
.house--right{left:0;top:296px;width:120px;height:194px}
.rule{position:absolute;left:0;right:0;bottom:14px;height:4px;background:var(--red)}
</style>
</head>
<body>

<section class="spread spread--outer">
  <article class="page back">
    <div class="back__band"></div>
    <div class="back__body">
      <h2 class="heading back__title">How do you get started?</h2>
      <p>First contact us. Then we'll send you an application to fill out. Within 24 hours we'll send you a quote and follow up via phone call to discuss details and answer any questions you might have, and then, finally, we'll send you our service agreement via email for your electronic signature.</p>
      <ul class="contact">
        <li><svg viewBox="0 0 16 16"><circle cx="8" cy="8" r="7" fill="none" stroke="#e2474d" stroke-width="1.4"/><path d="M8 4a3 3 0 0 1 3 3c0 2-3 5-3 5s-3-3-3-5a3 3 0 0 1 3-3z" fill="#e2474d"/></svg>Palm Crest Keeper LLC Honolulu Hawaii</li>
        <li><svg viewBox="0 0 16 16"><circle cx="8" cy="8" r="7" fill="none" stroke="#e2474d" stroke-width="1.4"/><path d="M5.5 4.5l1.5 0 .8 2-1 .8a5 5 0 0 0 2 2l.8-1 2 .8v1.5c-3 .6-6.7-3-6.1-6.1z" fill="#e2474d"/></svg><span class="phone">808-555-0142</span></li>
        <li><svg viewBox="0 0 16 16"><circle cx="8" cy="8" r="7" fill="none" stroke="#e2474d" stroke-width="1.4"/><rect x="4.5" y="5.5" width="7" height="5" fill="none" stroke="#e2474d"/><path d="M4.5 5.5l3.5 3 3.5-3" fill="none" stroke="#e2474d"/></svg>hello@palmcrestkeeper.com</li>
        <li><svg viewBox="0 0 16 16"><circle cx="8" cy="8" r="7" fill="none" stroke="#e2474d" stroke-width="1.4"/><circle cx="8" cy="8" r="3.5" fill="none" stroke="#e2474d"/><path d="M4.5 8h7M8 4.5v7" stroke="#e2474d"/></svg>www.palmcrestkeeper.com</li>
      </ul>
      <div class="badge" role="img" aria-label="Accreditation badge"></div>
      <p class="back__note">We are Accredited Members of the CHCG. We are insured and bonded, and we agreed to uphold the strictest and most ethical standards in the industry.</p>
    </div>
  </article>

  <article class="page front">
    <div class="front__photo" role="img" aria-label="Photo of a white Hawaiian villa with an infinity pool, palm trees and ocean under a blue sky"></div>
    <div class="front__strip"></div>
    <div class="brand"><span class="brand__mark"></span><span class="brand__name">Palm Crest Keeper</span></div>
    <div class="brand__tag">Your Home Watch Company</div>
    <h1 class="front__title">Providing Premiere Home Watch and Concierge Services</h1>
  </article>
</section>

<section class="spread spread--inner">
  <article class="page inside-left">
    <div class="band band--left">
      <h2 class="heading band__title">What do we do?</h2>
      <p>We save your time. We perform visual inspections and provide our presence while you are away so you can enjoy your time and home while you are on the island. We have your back!</p>
    </div>
    <div class="devices" role="img" aria-label="Laptop and tablet showing a home photo and an inspection checklist"></div>
    <div class="services">
      <div class="service">
        <h3 class="service__title">General Outdoor Visual Inspections</h3>
        <p>Check yard, lawn and landscaping; check lanai, deck, and pool area for any damage; check for mold or fading of all outdoor furniture; check water level of swimming pool or hot tub, if applicable</p>
      </div>
      <div class="service">
        <h3 class="service__title">Home Exterior Visual Inspections</h3>
        <p>Check security cameras; check for overall damage; remove mail, newspapers, and flyers from mailbox and store inside of the property; check outdoor plumbing and hoses for leakage; check garage; check for vandalism and theft</p>
      </div>
      <div class="service">
        <h3 class="service__title">Home Interior Visual Inspections</h3>
        <p>Make sure security system is in working order; ensure that all doors, windows and sliders are locked and secured; check thermostats and make sure the air conditioning is set at appropriate and requested temperature; make sure all smoke detectors are in proper working order or replace batteries if necessary; visually inspect the water heater and washer and dryer</p>
      </div>
    </div>
    <div class="house house--left" role="img" aria-label="Cutaway illustration of a two-storey house with service icons"></div>
    <div class="rule"></div>
  </article>

  <article class="page inside-right">
    <div class="band band--right">
      <p>Don't let repairs or unexpected surprises upon your arrival take away from your vacation time. Arrive knowing all you need to do in Hawaii is relax and enjoy your second home and the island.</p>
    </div>
    <div class="tab">Concierge Services</div>
    <div class="concierge">
      <div class="service">
        <h3 class="service__title">Pre-Arrival</h3>
        <p>Groceries purchased and stored, air conditioning and ceiling vents turned on and/or windows opened, water turned on, flowers placed, fresh laundered linens on beds, towels arranged in the bathrooms, deck furniture placed on decks and patio, house freshened up and aired out, security system disarmed as appropriate, decks, walkways, lanais, and driveways cleared of debris and special requests completed.</p>
      </div>
      <div class="service">
        <h3 class="service__title">Post-Departure</h3>
        <p>House cleaning coordinated, beds made, sheets and towels cleaned, dishes washed and put away, all doors and windows secured, lights on timers set, water turned off, outdoor furniture stored or covered per specific instructions, driveways, lanais, walkways and decks cleared of debris, air conditioning set to appropriate level, trash placed for collection and security system turned on.</p>
      </div>
      <div class="service service--wide">
        <h3 class="service__title">Sample of Special Services/Requests</h3>
        <p>Key holding services, mail forwarding, coordination of transportation from and to the airport, light handyman and landscaping services, vendor coordination (we coordinate access and meet everyone you authorize at your home including but not limited to maintenance, repair, pest control, landscaping and tree trimming, and utility providers), pre-storm services (secure outdoor furniture, potted plants, hammocks and any other outdoor items, etc.) and post-storm services (clean walkway and driveway, pick-up trash, etc.), and emergency services response, etc.</p>
      </div>
    </div>
    <div class="house house--right" role="img" aria-label="Cutaway house illustration continued with garden tree"></div>
    <div class="rule"></div>
  </article>
</section>

</body>
</html>
```